" Nome da empresa: Recanto Vivale CLINICA DE NUTRIÇAO SOMOS NUTRICIONISTAS E DESEJAMOS PROPORCIONAR AOS NOSSOS PACIENTES UM TRATAMENTO INDIVIDUALIZADO. FAREMOS ATENDIMENTOS NUTRICIONAIS A FIM DE LEVAR QUALIDADE DE VIDA E PREVENÇAO de doenças, focando na educaçao nutricional "

```html
<!DOCTYPE html>
<html lang="pt-BR">
<head>
<meta charset="UTF-8">
<title>Recanto Vivale — Papel Timbrado</title>
<link href="https://fonts.googleapis.com/css2?family=Nunito:wght@400;600&display=swap" rel="stylesheet">
<style>
  :root {
    --backdrop: #ece7e1;
    --paper: #ffffff;
    --brand-green: #1f5a50;
    --brand-orange: #f0a23a;
    --accent-soft: #fbe3bd;
    --footer-grey: #6c6c6c;
  }
  * { margin: 0; padding: 0; box-sizing: border-box; }
  html, body {
    width: 1200px;
    height: 1200px;
    overflow: hidden;
    background: var(--backdrop);
    font-family: "Nunito", sans-serif;
  }
  .letterhead {
    position: absolute;
    left: 233px;
    top: 100px;
    width: 734px;
    height: 1000px;
    background: var(--paper);
    box-shadow: 0 4px 18px rgba(0, 0, 0, 0.12);
  }
  .letterhead__band {
    position: absolute;
    left: 0;
    top: 0;
    width: 18px;
    height: 100%;
    background: var(--brand-green);
  }
  .brand {
    position: absolute;
    top: 40px;
    left: 0;
    width: 100%;
    display: flex;
    flex-direction: column;
    align-items: center;
    gap: 10px;
  }
  .brand__dot {
    width: 34px;
    height: 34px;
    border-radius: 50%;
    background: var(--brand-orange);
  }
  .brand__name {
    font-size: 30px;
    font-weight: 600;
    color: var(--brand-green);
    letter-spacing: 0.2px;
  }
  .letterhead__accent {
    position: absolute;
    right: 50px;
    bottom: 70px;
    width: 210px;
    height: 210px;
    border-radius: 50%;
    background: var(--accent-soft);
  }
  .letterhead__footer {
    position: absolute;
    left: 50px;
    bottom: 26px;
    font-size: 11px;
    color: var(--footer-grey);
    white-space: nowrap;
  }
</style>
</head>
<body>
  <main class="letterhead">
    <div class="letterhead__band"></div>
    <header class="brand">
      <span class="brand__dot"></span>
      <span class="brand__name">Recanto Vivale</span>
    </header>
    <div class="letterhead__accent"></div>
    <footer class="letterhead__footer">
      Telefone 4020-7315 / Email contato@recantovivale.com.br / Rua das Acácias, 48 Jardim Aurora Cidade Serena
    </footer>
  </main>
</body>
</html>
```